Harborline Motors LLC

Car Dealer Customer Service
Address: 2741 Linden Avenue, Shelbyville, TN 37162
web: www.harborlinemotorstn.net
email: harborlinemotorstn@mailbox-example.net
Phone: (931) 555-0148
Phone: (629) 555-0173

```html
<!DOCTYPE html>
<html lang="en">
<head>
<meta charset="utf-8">
<title>Harborline Motors – Business Card</title>
<link rel="stylesheet" href="https://fonts.googleapis.com/css2?family=Montserrat:wght@800&family=Roboto:wght@500;700&display=swap">
<style>
  :root {
    --backdrop: #2b2b2b;
    --card: #ffffff;
    --blue: #2b8fcb;
    --blue-dark: #1f6fa8;
    --orange: #f0b13a;
    --orange-deep: #e6a02a;
    --peach: #f7e4c8;
    --white: #ffffff;
  }
  * { box-sizing: border-box; margin: 0; padding: 0; }
  html, body { width: 1200px; height: 900px; overflow: hidden; }
  body { background: var(--backdrop); font-family: "Roboto", Arial, sans-serif; position: relative; }

  .card {
    position: absolute; left: 260px; width: 680px; height: 389px;
    background: var(--card); overflow: hidden; border-radius: 4px;
    box-shadow: 0 10px 30px rgba(0,0,0,0.35);
  }
  .card--back { top: 41px; }
  .card--front { top: 470px; }

  /* back */
  .back-illustration {
    position: absolute; left: 60px; top: 20px; width: 560px; height: 330px;
    background: radial-gradient(ellipse 50% 48% at 50% 50%, var(--peach) 0%, rgba(247,228,200,0.75) 45%, rgba(247,228,200,0) 100%);
  }
  .back-brand {
    position: absolute; left: 0; right: 0; top: 92px;
    display: flex; flex-direction: column; align-items: center;
  }
  .back-brand .mark {
    width: 118px; height: 118px; border-radius: 50%;
    background: var(--blue); margin-bottom: 18px;
  }
  .back-brand .name {
    font-family: "Montserrat", Arial, sans-serif; font-weight: 800;
    font-size: 36px; color: var(--blue-dark); text-transform: uppercase; letter-spacing: 0.5px; line-height: 1;
  }
  .back-brand .tagline {
    font-family: "Montserrat", Arial, sans-serif; font-weight: 800;
    font-size: 13px; color: var(--orange); text-transform: uppercase; letter-spacing: 1px; margin-top: 8px;
  }

  /* front */
  .front-mark {
    position: absolute; left: 40px; top: 62px; width: 190px;
    display: flex; flex-direction: column; align-items: center;
  }
  .front-mark .mark {
    width: 150px; height: 150px; border-radius: 50%; background: var(--blue);
  }
  .front-mark .name {
    margin-top: 12px; text-align: center;
    font-family: "Montserrat", Arial, sans-serif; font-weight: 800;
    font-size: 15px; line-height: 1.2; color: var(--blue-dark); text-transform: uppercase; letter-spacing: 0.5px;
  }
  .front-info { position: absolute; left: 262px; top: 34px; }
  .front-info .name {
    font-family: "Montserrat", Arial, sans-serif; font-weight: 800;
    font-size: 27px; color: var(--blue-dark); text-transform: uppercase; line-height: 1;
  }
  .front-info .tagline {
    font-weight: 500; font-size: 14px; color: var(--orange); margin: 5px 0 16px;
  }
  .contact { display: flex; align-items: flex-start; gap: 9px; margin-bottom: 11px;
    font-weight: 700; font-size: 16px; color: var(--blue-dark); letter-spacing: 0.3px; line-height: 1.25; }
  .contact svg { flex: none; width: 20px; height: 20px; margin-top: 1px; }

  .front-illustration {
    position: absolute; left: 566px; top: 214px; width: 100px; height: 74px;
    background: radial-gradient(ellipse 50% 50% at 50% 55%, var(--orange) 0%, rgba(240,177,58,0.55) 60%, rgba(240,177,58,0) 100%);
  }
  .accent-line { position: absolute; left: 0; right: 0; top: 294px; height: 5px; background: var(--orange); }
  .phone-band {
    position: absolute; left: 0; right: 0; top: 307px; bottom: 0; background: var(--blue);
    display: flex; align-items: center; gap: 16px; padding-left: 28px;
    color: var(--white); font-weight: 700; font-size: 33px; letter-spacing: 1.5px;
  }
  .phone-band svg { width: 40px; height: 40px; flex: none; }
</style>
</head>
<body>

<section class="card card--back" aria-label="Business card, back">
  <div class="back-illustration" role="img" aria-label="Faint large vintage car illustration in soft peach"></div>
  <div class="back-brand">
    <span class="mark" aria-hidden="true"></span>
    <div class="name">Harborline Motors</div>
    <div class="tagline">Car Dealer Customer Service</div>
  </div>
</section>

<section class="card card--front" aria-label="Business card, front">
  <div class="front-mark">
    <span class="mark" aria-hidden="true"></span>
    <div class="name">Harborline<br>Motors</div>
  </div>

  <div class="front-info">
    <div class="name">Harborline Motors</div>
    <div class="tagline">Car Dealer Customer Service</div>

    <div class="contact">
      <svg viewBox="0 0 20 20" aria-hidden="true"><circle cx="10" cy="10" r="9" fill="none" stroke="#1f6fa8" stroke-width="1.6"/><path d="M10 4.5a3.4 3.4 0 0 0-3.4 3.4c0 2.5 3.4 6.6 3.4 6.6s3.4-4.1 3.4-6.6A3.4 3.4 0 0 0 10 4.5zm0 4.7a1.3 1.3 0 1 1 0-2.6 1.3 1.3 0 0 1 0 2.6z" fill="#1f6fa8"/></svg>
      <span>2741 Linden Avenue,<br>Shelbyville, TN 37162</span>
    </div>
    <div class="contact">
      <svg viewBox="0 0 20 20" aria-hidden="true"><circle cx="10" cy="10" r="9" fill="none" stroke="#1f6fa8" stroke-width="1.6"/><rect x="5" y="6.5" width="10" height="7" rx="1" fill="none" stroke="#1f6fa8" stroke-width="1.4"/><path d="M5.3 7l4.7 3.6L14.7 7" fill="none" stroke="#1f6fa8" stroke-width="1.4"/></svg>
      <span>harborlinemotorstn@mailbox-example.net</span>
    </div>
    <div class="contact">
      <svg viewBox="0 0 20 20" aria-hidden="true"><circle cx="10" cy="10" r="9" fill="none" stroke="#1f6fa8" stroke-width="1.6"/><circle cx="10" cy="10" r="5" fill="none" stroke="#1f6fa8" stroke-width="1.3"/><ellipse cx="10" cy="10" rx="2.2" ry="5" fill="none" stroke="#1f6fa8" stroke-width="1.2"/><path d="M5 10h10" stroke="#1f6fa8" stroke-width="1.2"/></svg>
      <span>www.harborlinemotorstn.net</span>
    </div>
  </div>

  <div class="front-illustration" role="img" aria-label="Small orange vintage car illustration"></div>
  <div class="accent-line"></div>
  <div class="phone-band">
    <svg viewBox="0 0 40 40" aria-hidden="true"><circle cx="20" cy="20" r="18" fill="none" stroke="#fff" stroke-width="2.5"/><path d="M14.5 11.5l3 .3 1.6 4.3-2 1.7a11 11 0 0 0 5.1 5.1l1.7-2 4.3 1.6.3 3c-.3 1.5-1.8 2.4-3.3 2.2C18.4 26.8 13.2 21.6 12.3 14.8c-.2-1.5.7-3 2.2-3.3z" fill="#fff"/></svg>
    <span>(931) 555-0148 / (629) 555-0173</span>
  </div>
</section>

</body>
</html>
```